Business Card Design

We need a new business card design for our company, BrightRow7.

Our website: www.brightrow7.ca

We are open to all ideas, from professional to very creative.
Updates

Design update requests:

1. We would like to see some examples with "BrightRow7" instead of "BrightRow7" as the company name.
2. Would like to see "Software | Web | Branding" included on the card somewhere as well.

Thanks.

We are really trying to express the nature of our business through our business card.  "Lumen" can be misconstrued for the health industry, so use of "BrightRow7" and the "Software | Web | Branding" slogan are key to understanding our business.

We have uploaded a new PSD which includes a monitor, tablet, and phone screen.  This represents the flexibility of web applications and is another tool we would like to see used on business cards.

We will be eliminating designs today and will await updated designs with these new specs.

Thank-you.

Industry/Entity Type

Business

Requirements
Must have
• Content:
First M. Last
Managing Partner
e. email@brightrow7.ca
p. 555.555.5555

```html
<!DOCTYPE html>
<html lang="en">
<head>
<meta charset="utf-8">
<title>BrightRow7 – Business Card</title>
<link rel="stylesheet" href="https://fonts.googleapis.com/css2?family=Arimo:wght@400;700&display=swap">
<style>
  :root {
    --backdrop: #e8ebed;
    --card: #ffffff;
    --blue-dark: #1f5f85;
    --blue-mid: #1189cf;
    --blue-light: #86c6e8;
    --ink: #3f4347;
    --ink-soft: #6b7075;
    --icon: #7d8a94;
  }
  * { box-sizing: border-box; margin: 0; padding: 0; }
  html, body {
    width: 1200px;
    height: 864px;
    overflow: hidden;
    background: var(--backdrop);
    font-family: "Arimo", Arial, sans-serif;
    color: var(--ink);
  }
  .card {
    position: absolute;
    top: 277px;
    width: 540px;
    height: 309px;
    background: var(--card);
    overflow: hidden;
    box-shadow: 0 2px 10px rgba(0, 0, 0, 0.12);
  }
  .card--front { left: 40px; }
  .card--back { left: 620px; }

  .mosaic-area {
    position: absolute;
    background: linear-gradient(135deg, var(--blue-dark) 0%, var(--blue-mid) 50%, var(--blue-light) 100%);
  }
  .card--front .mosaic-area { left: 0; top: 0; width: 260px; height: 150px; }
  .card--back .mosaic-area { right: 0; top: 88px; width: 150px; height: 172px; }

  .brand {
    position: absolute;
    display: flex;
    align-items: center;
    color: var(--ink);
  }
  .brand__mark { background: var(--blue-mid); display: block; flex: none; }
  .brand__text { display: flex; flex-direction: column; }
  .brand__name { font-weight: 700; letter-spacing: 0.5px; line-height: 1; }
  .brand__slogan { font-weight: 700; color: var(--ink); letter-spacing: 1px; text-transform: uppercase; }

  .card--front .brand { right: 44px; bottom: 50px; gap: 12px; }
  .card--front .brand__mark { width: 40px; height: 40px; }
  .card--front .brand__name { font-size: 30px; }
  .card--front .brand__slogan { font-size: 10px; margin-top: 5px; }

  .card--back .brand { left: 32px; top: 20px; gap: 7px; }
  .card--back .brand__mark { width: 20px; height: 20px; }
  .card--back .brand__name { font-size: 15px; }
  .card--back .brand__slogan { font-size: 6.5px; margin-top: 3px; letter-spacing: 0.6px; }

  .contact { position: absolute; left: 32px; top: 64px; }
  .contact__name { font-size: 23px; font-weight: 400; color: var(--ink); }
  .contact__role { font-size: 12px; color: var(--ink); margin-top: 2px; }
  .contact__lines { margin-top: 14px; font-size: 12.5px; line-height: 1.35; color: var(--ink-soft); }

  .socials {
    position: absolute;
    left: 32px;
    right: 32px;
    bottom: 18px;
    display: flex;
    justify-content: space-between;
    font-size: 9px;
    color: var(--ink-soft);
  }
  .social { display: flex; align-items: center; gap: 5px; }
  .social__icon { width: 10px; height: 10px; background: var(--icon); border-radius: 2px; }
</style>
</head>
<body>

<section class="card card--front">
  <div class="mosaic-area" role="img" aria-label="Decorative blue tile mosaic area"></div>
  <div class="brand">
    <span class="brand__mark"></span>
    <span class="brand__text">
      <span class="brand__name">BrightRow7</span>
      <span class="brand__slogan">Software | Web | Branding</span>
    </span>
  </div>
</section>

<section class="card card--back">
  <div class="brand">
    <span class="brand__mark"></span>
    <span class="brand__text">
      <span class="brand__name">BrightRow7</span>
      <span class="brand__slogan">Software | Web | Branding</span>
    </span>
  </div>
  <div class="contact">
    <h1 class="contact__name">Jane R. Roe</h1>
    <p class="contact__role">Managing Partner</p>
    <p class="contact__lines">
      Your Street 123<br>
      e. email@brightrow7.ca<br>
      p. 555.555.5555<br>
      www.brightrow7.ca
    </p>
  </div>
  <div class="mosaic-area" role="img" aria-label="Decorative blue tile mosaic area"></div>
  <div class="socials">
    <span class="social"><span class="social__icon"></span>name/friendloop.com</span>
    <span class="social"><span class="social__icon"></span>name/chirpline.com</span>
    <span class="social"><span class="social__icon"></span>name/circlesnet.com</span>
  </div>
</section>

</body>
</html>
```